INNOVATIVE DESIGN NEEDED FOR FINANCIAL COMPANY

INTERNATIONAL FIRM IN HONG KONG NEEDS A MODERN BUSINESS CARD DESIGN. ONE SIDE ENGLISH OTHER SIDE IN CHINESE. WE ARE OPEN TO CHANGING FONTS AND COLOR. SHOULD BE A CARD THAT IS PROFESSIONAL DEALING WITH HIGH NET WORTH CLIENTELE. BOTH SIDES OF THE CARD WILL BE THE SAME, HOWEVER, THE WORDING ON ONE SIDE WILL BE ENGLISH AND THE OTHER SIDE IN CHINESE (CAN ASSIST IN THE LETTERING - CAN PROVIDE ONCE CARD DESIGN IS ACCEPTED.

Target Market(s)

Hong Kong/CHINA

Contact Information for Business Card

ATTRACTIVE MODERN

```html
<!DOCTYPE html>
<html lang="en">
<head>
<meta charset="utf-8">
<title>Cedarline Asset Management – Business Card</title>
<link rel="stylesheet" href="https://fonts.googleapis.com/css2?family=Montserrat:wght@400;500;600&family=Noto+Sans+TC:wght@500;900&family=Noto+Serif+TC:wght@400;500&display=swap">
<style>
  :root {
    --bg: #e9e7e3;
    --paper: #fbfbfa;
    --slate: #2d3434;
    --slate-light: #3f4747;
    --green: #17a27a;
    --ink: #3a3f3f;
    --ink-soft: #5d6363;
    --white: #ffffff;
  }
  * { margin: 0; padding: 0; box-sizing: border-box; }
  html, body { width: 1200px; height: 900px; overflow: hidden; }
  body {
    background: var(--bg);
    font-family: "Montserrat", sans-serif;
    position: relative;
  }
  .card {
    position: absolute;
    width: 560px;
    height: 320px;
    border-radius: 4px;
    box-shadow: 0 10px 30px rgba(0,0,0,.18);
    overflow: hidden;
  }
  .card--chinese { left: 30px; top: 150px; background: var(--paper); color: var(--ink); }
  .card--english {
    left: 610px; top: 430px;
    background: radial-gradient(circle at 30% 25%, var(--slate-light), var(--slate) 70%);
    color: var(--white);
  }
  .brand {
    position: absolute; left: 34px; top: 32px;
    display: flex; align-items: center; gap: 12px;
  }
  .brand__mark {
    width: 40px; height: 40px; border-radius: 50%;
    background: var(--green); flex: none;
  }
  .brand__name { font-weight: 600; line-height: 1.15; }
  .brand__zh { font-family: "Noto Sans TC", sans-serif; font-weight: 900; font-size: 24px; letter-spacing: 1px; display: block; }
  .brand__en { font-family: "Noto Sans TC", sans-serif; font-weight: 900; font-size: 10.5px; letter-spacing: 1.4px; display: block; }
  .card--chinese .brand__name { color: var(--ink); }
  .card--english .brand__name { color: var(--white); }
  .divider {
    position: absolute; left: 34px; right: 34px; top: 160px;
    height: 2px; background: var(--green);
  }
  .contacts {
    position: absolute; left: 34px; top: 178px;
    list-style: none; font-size: 12px; line-height: 19px;
  }
  .contacts li { display: flex; align-items: center; gap: 8px; }
  .contacts svg { width: 11px; height: 11px; fill: var(--green); flex: none; }
  .card--chinese .contacts { color: var(--ink-soft); }
  .holder {
    position: absolute; right: 34px; top: 98px; text-align: right;
  }
  .holder__name { color: var(--green); }
  .card--chinese .holder__name { font-family: "Noto Serif TC", serif; font-size: 24px; letter-spacing: 3px; font-weight: 500; }
  .card--chinese .holder__title { font-family: "Noto Serif TC", serif; font-size: 16px; letter-spacing: 3px; color: var(--ink-soft); }
  .card--english .holder { top: 96px; }
  .card--english .holder__name { font-size: 25px; font-weight: 600; letter-spacing: 1px; line-height: 1.1; }
  .card--english .holder__title { font-size: 16px; letter-spacing: 1px; }
  .address {
    position: absolute; right: 34px; top: 178px; text-align: right;
    font-size: 13px; line-height: 19px;
  }
  .card--chinese .address { font-family: "Noto Serif TC", serif; letter-spacing: 2px; color: var(--ink-soft); }
  .card--english .address { letter-spacing: .5px; }
</style>
</head>
<body>

<svg width="0" height="0" style="position:absolute">
  <defs>
    <symbol id="icon-phone" viewBox="0 0 24 24"><path d="M6.6 10.8a15.1 15.1 0 0 0 6.6 6.6l2.2-2.2c.3-.3.7-.4 1-.2 1.1.4 2.3.6 3.6.6.6 0 1 .4 1 1V20c0 .6-.4 1-1 1C10.6 21 3 13.4 3 4c0-.6.4-1 1-1h3.5c.6 0 1 .4 1 1 0 1.3.2 2.5.6 3.6.1.3 0 .7-.2 1z"/></symbol>
    <symbol id="icon-mail" viewBox="0 0 24 24"><path d="M2 5h20v14H2zm2 2v.5l8 5 8-5V7zm0 2.8V17h16V9.8l-8 5z"/></symbol>
    <symbol id="icon-globe" viewBox="0 0 24 24"><path d="M12 2a10 10 0 1 0 0 20 10 10 0 0 0 0-20zm6.9 9h-3a15 15 0 0 0-1.2-5.6A8 8 0 0 1 18.9 11zM12 4.1c.9 1.3 1.7 3.6 1.9 6.9h-3.8c.2-3.3 1-5.6 1.9-6.9zM9.3 5.4A15 15 0 0 0 8.1 11h-3a8 8 0 0 1 4.2-5.6zM5.1 13h3a15 15 0 0 0 1.2 5.6A8 8 0 0 1 5.1 13zm6.9 6.9c-.9-1.3-1.7-3.6-1.9-6.9h3.8c-.2 3.3-1 5.6-1.9 6.9zm2.7-1.3a15 15 0 0 0 1.2-5.6h3a8 8 0 0 1-4.2 5.6z"/></symbol>
  </defs>
</svg>

<section class="card card--chinese" lang="zh-Hant">
  <div class="brand">
    <span class="brand__mark"></span>
    <span class="brand__name">
      <span class="brand__zh">雪松資產管理有限公司</span>
      <span class="brand__en" lang="en">Cedarline Asset Management Ltd</span>
    </span>
  </div>
  <div class="holder">
    <div class="holder__name">林丹尼</div>
    <div class="holder__title">經理</div>
  </div>
  <div class="divider"></div>
  <ul class="contacts" lang="en">
    <li><svg><use href="#icon-phone"/></svg>852-555-0148</li>
    <li><svg><use href="#icon-mail"/></svg>daniel.lam@cedarline-am.com</li>
    <li><svg><use href="#icon-globe"/></svg>www.cedarline-am.com</li>
  </ul>
  <div class="address">香港九龍彌敦道<br>海景大廈12號</div>
</section>

<section class="card card--english">
  <div class="brand">
    <span class="brand__mark"></span>
    <span class="brand__name">
      <span class="brand__zh" lang="zh-Hant">雪松資產管理有限公司</span>
      <span class="brand__en">Cedarline Asset Management Ltd</span>
    </span>
  </div>
  <div class="holder">
    <div class="holder__name">DANIEL LAM</div>
    <div class="holder__title">Manager</div>
  </div>
  <div class="divider"></div>
  <ul class="contacts">
    <li><svg><use href="#icon-phone"/></svg>852-555-0148</li>
    <li><svg><use href="#icon-mail"/></svg>daniel.lam@cedarline-am.com</li>
    <li><svg><use href="#icon-globe"/></svg>www.cedarline-am.com</li>
  </ul>
  <div class="address">12 Harbourview Tower<br>Nathan Rd, HONG KONG</div>
</section>

</body>
</html>
```